HiItsJonBrell.com needs a modern, eye-catching business card design

My name is Jon Brell and I own a video training (software development industry) website. I need a business card design that is eye catching for when I travel to conferences or do seminars. I would prefer something simple but bold. Something along the lines of this: https://pixvaultstatic.example/gallery_img/530172/44018/44018_9917302_530172_image.jpg

Note that I do not have a specific logo, but I do have an caricature I use on my site of myself. I've not attached it because I'm not really a fan of having it on my business cards. I would prefer lettering instead of an image. You can go to my website (https://hiitsjonbrell.com) for inspiration.

I want to add the following information on my card (the order of these, their size, and their casing is up to you):

Jon Brell
jon@HiItsJonBrell.com
@HiItsJonBrell
HiItsJonBrell.com
vidsharehub.example/HiItsJonBrell

I would also like to have somewhere on the card a small ad that says "Get a free course at https://HiItsJonBrell.com/FreeCourse". Feel free to play with that wording or layout if you need. I would prefer this text to be at the bottom of the card and subtle. Some small eye-catching thing might be ok but nothing huge or garish.

I plan on printing this card at pressquill.example (https://www.pressquill.example/us/design-guidelines/business-cards.html). I would like it to be the standard size (3.66" x 2.16"). I would prefer rounded corners and horizontal orientation. This is a two-side design. I would prefer the side with all of the information be primarily white but I like color text (again, flexible on that). On the front side, I like simple. Maybe just HiItsJonBrell.com (casing on that is up to you - whatever looks and reads the best - that goes for all of the casing). As for font choices, I prefer a modern, clean font. For example, Open Sans Light can be a nice option.

Website Info (might be helpful for the card):
Color Palette

Darkest blue - #263246
Alternate blue - #2F4E6A
Light blue - #2A98C3
Orange - #FF6201
White - #FFFFFF

Font for Jon Brell Logo

Jellyka Estryas Handwriting
http://www.typecrate.example/jellyka_estryas_handwriting.font

Fonts for Site Content and VidShare Thumbnails

Lovelo (bold title font)
http://www.glyphmill.example/lovelo-font/

Open Sans (body font)
http://www.letterbarn.example/fonts/open-sans

Industry/Entity Type

Software Development

Contact Information for Business Card

Jon Brell
jon@HiItsJonBrell.com
@HiItsJonBrell
HiItsJonBrell.com
vidsharehub.example/HiItsJonBrell

Get a free course at https://HiItsJonBrell.com/FreeCourse

Colors

Designer to choose colors to be used in the design.

Requirements
Nice to have
• Modern color - maybe primarily a color on the front and then that color as an accent on the back.
Should not have
• Lots of colors - I LOVE color but do not want a rainbow of colors on the card.

```html
<!DOCTYPE html>
<html lang="en">
<head>
<meta charset="utf-8">
<title>Jon Brell – Business Card</title>
<link rel="stylesheet" href="https://fonts.googleapis.com/css2?family=Open+Sans:wght@300;400;600;700&display=swap">
<style>
  :root {
    --page-bg: #e9e6e1;
    --card-white: #ffffff;
    --card-dark: #1d2022;
    --ink-dark: #2b2b2b;
    --ink-light: #f2f2f2;
    --accent-blue: #2a6f93;
    --accent-bright: #2a98c3;
    --rule-grey: #8a8a8a;
    --mark-blue-soft: #dcebf2;
    --mark-blue-mid: #b9d6e4;
    --mark-dark-a: #26323a;
    --mark-dark-b: #2e4a5c;
  }
  * { box-sizing: border-box; margin: 0; padding: 0; }
  html, body { width: 1200px; height: 911px; overflow: hidden; }
  body {
    background: var(--page-bg);
    font-family: "Open Sans", Arial, sans-serif;
    position: relative;
  }
  .card {
    position: absolute;
    width: 540px;
    height: 319px;
    border-radius: 22px;
    box-shadow: 0 10px 28px rgba(0,0,0,.22);
    overflow: hidden;
  }
  .card--info { left: 40px; top: 296px; background: var(--card-white); color: var(--ink-dark); }
  .card--front { left: 620px; top: 296px; background: var(--card-dark); color: var(--ink-light); }

  /* info side */
  .info__portrait {
    position: absolute; left: 278px; top: 52px; width: 78px; height: 78px;
    border-radius: 50%;
    background: radial-gradient(circle at 40% 35%, var(--mark-blue-soft), var(--mark-blue-mid));
  }
  .info__signature {
    position: absolute; left: 370px; top: 36px; width: 138px; height: 70px;
    border-radius: 35px;
    background: linear-gradient(100deg, var(--mark-blue-soft), rgba(220,235,242,0));
  }
  .info__rule {
    position: absolute; left: 32px; right: 32px; top: 146px; height: 1px; background: var(--rule-grey);
  }
  .info__contact {
    position: absolute; right: 34px; top: 160px; text-align: right;
    font-size: 14px; line-height: 22px;
  }
  .info__name {
    position: absolute; left: 34px; bottom: 74px;
    font-weight: 700; font-size: 25px; line-height: 30px; color: var(--accent-blue); letter-spacing: -.3px;
  }
  .info__socials { position: absolute; left: 36px; bottom: 28px; font-size: 13px; line-height: 19px; }
  .social { display: flex; align-items: center; gap: 6px; }
  .social__dot { width: 11px; height: 11px; border-radius: 50%; background: var(--accent-blue); flex: none; }

  /* front side */
  .front__portrait {
    position: absolute; left: 44px; top: 34px; width: 112px; height: 112px;
    border-radius: 50%;
    background: radial-gradient(circle at 40% 35%, var(--mark-dark-b), var(--mark-dark-a));
  }
  .front__signature {
    position: absolute; left: 232px; top: 96px; width: 268px; height: 112px;
    border-radius: 56px;
    background: linear-gradient(100deg, rgba(255,255,255,.10), rgba(255,255,255,0));
  }
  .front__ad { position: absolute; left: 40px; bottom: 30px; font-size: 13px; line-height: 20px; }
  .front__ad-line { display: block; width: 240px; height: 1px; background: linear-gradient(90deg, rgba(255,255,255,.7), rgba(255,255,255,0)); margin: 6px 0; }
  .front__ad-title { color: var(--accent-bright); font-weight: 600; font-size: 16px; line-height: 22px; }
</style>
</head>
<body>
  <section class="card card--info" aria-label="Information side">
    <div class="info__portrait" role="img" aria-label="Portrait artwork area"></div>
    <div class="info__signature" role="img" aria-label="Handwritten Jon Brell signature"></div>
    <div class="info__rule"></div>
    <div class="info__contact">
      <p>jon@HiItsJonBrell.com</p>
      <p>HiItsJonBrell.com</p>
    </div>
    <h1 class="info__name">Jon Brell</h1>
    <div class="info__socials">
      <p class="social"><span class="social__dot"></span>@HiItsJonBrell</p>
      <p class="social"><span class="social__dot"></span>HiItsJonBrell</p>
    </div>
  </section>

  <section class="card card--front" aria-label="Front side">
    <div class="front__portrait" role="img" aria-label="Portrait artwork area"></div>
    <div class="front__signature" role="img" aria-label="Handwritten Jon Brell signature in white"></div>
    <div class="front__ad">
      <p class="front__ad-title">Get a free course at</p>
      <p>https://HiItsJonBrell.com/FreeCourse</p>
      <span class="front__ad-line"></span>
      <p>www.HiItsJonBrell.com</p>
    </div>
  </section>
</body>
</html>
```